依頼詳細
第一回公演のチラシデザインを依頼したいです。

初回公演のタイトルは「日々硝子」

人は生きているだけで無数のドラマを生み出す。
それはその人に取っては重要で、他人にとっては些細な一面。
誰にもいうことはないけれど、自分の中で確かに起きる数々の感情の変化。
友情、恋愛、家族、夢。
何が人を作り、何が人を動かすのか。
誰かの長い人生のほんの一部を切り取り並べた『日々硝子』
あなたの中にもきっとある。
そんな感情のストーリー。

このようなテーマのダンス公演です。

■チラシのイメージは
<表面>
「水彩画」
「ステージで1本のスポットライトを浴びている女性」
「タイトル文字」

<裏面>
表面のイメージを採用しつつ、下記記載事項を掲載して下さい。

裏面→イベント名、日程、アクセス
チケット料金、問い合わせ先
出演者の名前、スタッフクレジット、SNSへのQRコード

デザインの雰囲気は暗めで、
記載項目
【フライヤーの記載内容詳細】
・記載事項
表面
イベントタイトル「日々硝子」

裏面

イベント名:Dance Company PEX第一回公演「日々硝子」

日程:2022年9月3日(土)・4日(日)

アクセス:会場「ヴェルナ・ホール」
https://verna-hall.example/access/

チケット料金:¥3,000

問い合わせ先:公式インスタグラムよりDM

出演:ぬい/朝比奈澄/宇野咲良/辻堂早苗/森永つばさ/浜口紗英/桑原理恵/堀ゆずは/綾瀬千尋/今井澪/葛西陽一郎/北条美奈子/戸部和泉/菅野拓真

スタッフクレジット
制作:矢島紬/根本彩花/江藤まどか
振付:菅野拓真/ぬい/朝比奈澄/宇野咲良/葛西陽一郎/北条美奈子
照明:株式会社ペルカ
音響:杉浦晃司

SNSへのQRコード→インスタグラムURLはこちら
https://www.instagram.com/dancecompanypex/?igshid=QxRtUwVb9Z=

主催:株式会社VEN
サイズ
A5
ページ数
両面
希望イメージ
シンプル 複雑
単色 カラフル
暗い 明るい
日常 高級
遊び心 厳粛
未来的 伝統的
女性的 男性的
希望する色
青系、無彩色系
納品ファイル
• 高解像度JPG (.jpg)
• イラストレーター形式 (.ai)
補足説明
※記載事項の詳細につきましては現状仮となっております。
※添付ファイルについて
フライヤー表面のイメージ画像を添付しておりますので、色味や質感、雰囲気を参考にしていただけたらと思います。
ご確認を宜しくお願い致します。
■ 選んだ理由

こちらのイメージをしっかりと組んだ水彩画でのデザインをご提案くださいました。

■ 提案者全員のお礼・コメント

この度はコンペにご参加頂きありがとうございました。
素敵なデザインをご提案くださり大変助かりました!!

```html
<!DOCTYPE html>
<html lang="ja">
<head>
<meta charset="utf-8">
<title>日々硝子 — Dance Company PEX Vol.1</title>
<link href="https://fonts.googleapis.com/css2?family=Shippori+Mincho:wght@400;500&family=Cormorant+Garamond:wght@400&display=swap" rel="stylesheet">
<style>
  :root {
    --band: #2b2a2b;
    --paper: #d9d9d9;
    --wash-light: #e6e6e6;
    --wash-mid: #a9a9a9;
    --wash-dark: #4a4a4a;
    --ink: #1e1e1e;
    --white: #f7f7f7;
  }
  html, body {
    margin: 0;
    padding: 0;
    width: 847px;
    height: 1200px;
    overflow: hidden;
    background: var(--band);
  }
  .flyer {
    position: relative;
    width: 847px;
    height: 1200px;
    background: var(--band);
    overflow: hidden;
  }
  .watercolor {
    position: absolute;
    left: 0;
    top: 282px;
    width: 847px;
    height: 833px;
    background:
      radial-gradient(ellipse 320px 260px at 420px 140px, var(--wash-light) 0%, rgba(230,230,230,0) 100%),
      radial-gradient(ellipse 260px 200px at 120px 200px, rgba(90,90,90,0.55) 0%, rgba(90,90,90,0) 100%),
      radial-gradient(ellipse 300px 220px at 700px 380px, rgba(120,120,120,0.45) 0%, rgba(120,120,120,0) 100%),
      radial-gradient(ellipse 380px 230px at 300px 720px, rgba(60,60,60,0.75) 0%, rgba(60,60,60,0) 100%),
      radial-gradient(ellipse 300px 200px at 760px 760px, rgba(70,70,70,0.6) 0%, rgba(70,70,70,0) 100%),
      linear-gradient(180deg, var(--paper) 0%, var(--wash-mid) 55%, var(--wash-dark) 100%);
  }
  .title {
    position: absolute;
    left: 0;
    width: 100%;
    margin: 0;
    font-family: "Shippori Mincho", serif;
    font-weight: 400;
  }
  .title span {
    position: absolute;
    left: 404px;
    transform: translate(-50%, -50%);
    line-height: 1;
  }
  .title .lead {
    top: 212px;
    font-size: 118px;
    color: var(--white);
  }
  .title .rest {
    font-size: 68px;
    color: var(--ink);
  }
  .title .c2 { top: 367px; }
  .title .c3 { top: 480px; }
  .title .c4 { top: 599px; }
  .credit {
    position: absolute;
    left: 0;
    top: 1150px;
    width: 100%;
    text-align: center;
    font-family: "Cormorant Garamond", serif;
    font-size: 14px;
    letter-spacing: 0.42em;
    color: var(--white);
  }
</style>
</head>
<body>
  <main class="flyer">
    <div class="watercolor" role="img" aria-label="モノクロの水彩画：スポットライトを浴びてステージに立つ女性を思わせる、灰色のにじみ"></div>
    <h1 class="title" aria-label="日々硝子">
      <span class="lead">日</span>
      <span class="rest c2">々</span>
      <span class="rest c3">硝</span>
      <span class="rest c4">子</span>
    </h1>
    <p class="credit">Dance Company PEX&nbsp;&nbsp;Vol.1</p>
  </main>
</body>
</html>
```